Spa & Aesthetics business card design

Looking for business card designs for our spa. An excellent design would be able to be universally used by all employees - from staff to administrators to owners - and would be a simple but elegant depiction of a high end spa and aesthetics practice. We will be implementing a QR code on these cards, linked to our website. We are located in a desert setting so we would like to implement desert colors into our design (greens, hints of golds/beige, with a pop of color). We would also like to see some examples of embossed cards.
Should include:
Logo
First name, last name, credentials
Business address, phone number and email address
Space for QR code
Empty space on back to be able to hand write a short note or number as we hand out cards at events.
Please let me know if you need any additional info or formats of the design logo
high end cliental
see description

```html
<!DOCTYPE html>
<html lang="de">
<head>
<meta charset="utf-8">
<title>Solenne Spa &amp; Aesthetics – Visitenkarte</title>
<link rel="stylesheet" href="https://fonts.googleapis.com/css2?family=EB+Garamond:ital,wght@0,400;0,500;1,700&family=Montserrat:wght@500&display=swap">
<style>
  :root {
    --page: #f1efea;
    --card: #fdfbf6;
    --ink: #1f3a2e;
    --panel: #2f4a3a;
    --frame: #cdb98f;
    --line: #c2aa78;
    --accent: #d0674a;
    --on-dark: #fbf7ee;
  }
  * { margin: 0; padding: 0; box-sizing: border-box; }
  html, body { width: 1200px; height: 1200px; overflow: hidden; background: var(--page); }
  body { position: relative; font-family: "EB Garamond", Georgia, serif; color: var(--ink); }

  .card { position: absolute; left: 143px; width: 913px; height: 532px; background: var(--card); overflow: hidden; }
  .card--front { top: 56px; }
  .card--back { top: 621px; }

  .brand { position: absolute; transform: translate(-50%, -50%); text-align: center; white-space: nowrap; }
  .brand__name { font-weight: 500; color: var(--ink); letter-spacing: 0.28em; line-height: 1; margin-right: -0.28em; }
  .brand__tagline { display: flex; align-items: center; justify-content: center; gap: 12px; font-family: "Montserrat", Arial, sans-serif; font-weight: 500; letter-spacing: 0.2em; color: var(--ink); }
  .brand__tagline::before, .brand__tagline::after { content: ""; height: 1.5px; background: var(--accent); }
  .card--front .brand { left: 222px; top: 280px; }
  .card--front .brand__name { font-size: 48px; }
  .card--front .brand__tagline { font-size: 11px; margin-top: 12px; }
  .card--front .brand__tagline::before, .card--front .brand__tagline::after { width: 70px; }
  .card--back .brand { left: 438px; top: 285px; }
  .card--back .brand__name { font-size: 64px; }
  .card--back .brand__tagline { font-size: 14px; margin-top: 16px; gap: 16px; }
  .card--back .brand__tagline::before, .card--back .brand__tagline::after { width: 76px; }

  .qr-space { position: absolute; left: 182px; top: 400px; width: 80px; height: 80px; border: 2px dashed var(--line); }

  .panel { position: absolute; left: 445px; top: 44px; width: 468px; height: 444px; background: var(--panel); }
  .frame { position: absolute; border: 3px solid var(--frame); }
  .frame--large { left: 420px; top: 66px; width: 466px; height: 443px; }
  .frame--small { left: 381px; top: 25px; width: 94px; height: 90px; }

  .contact { position: absolute; inset: 0; color: var(--on-dark); }
  .contact__name { position: absolute; right: 61px; top: 108px; font-size: 33px; font-style: italic; font-weight: 700; white-space: nowrap; line-height: 1; }
  .contact__role { position: absolute; right: 61px; top: 142px; font-size: 20px; white-space: nowrap; line-height: 1; }
  .contact__line { position: absolute; right: 60px; font-size: 21px; line-height: 1; white-space: nowrap; display: flex; align-items: center; gap: 20px; transform: translateY(-50%); }
  .contact__line svg { width: 15px; height: 15px; flex: none; }
  .contact__line--phone { top: 226px; }
  .contact__line--mail { top: 265px; }
  .contact__line--web { top: 304px; }
  .contact__line--address { top: 401px; }

  .back-lines { position: absolute; inset: 0; width: 100%; height: 100%; }
</style>
</head>
<body>

<section class="card card--front" aria-label="Vorderseite">
  <div class="brand">
    <div class="brand__name">SOLENNE</div>
    <div class="brand__tagline">SPA &amp; AESTHETICS</div>
  </div>
  <div class="qr-space" aria-label="Platz für QR-Code"></div>
  <div class="panel"></div>
  <div class="frame frame--large"></div>
  <div class="frame frame--small"></div>
  <div class="contact">
    <p class="contact__name">Lorenz Albrecht</p>
    <p class="contact__role">Geschäftsführer</p>
    <p class="contact__line contact__line--phone">+49 1520 4837261
      <svg viewBox="0 0 16 16" aria-hidden="true"><path fill="var(--frame)" d="M3.5 1.5l2.5 0 1 3.5-1.6 1.2a8 8 0 0 0 4.4 4.4L11 9l3.5 1v2.5c0 1-1 2-2 2A11 11 0 0 1 1.5 3.5c0-1 1-2 2-2z"/></svg></p>
    <p class="contact__line contact__line--mail">lorenz@solennespa.com
      <svg viewBox="0 0 16 16" aria-hidden="true"><rect x="2" y="4" width="12" height="8" fill="var(--frame)"/><path d="M2 4l6 5 6-5" stroke="var(--panel)" stroke-width="1.2" fill="none"/></svg></p>
    <p class="contact__line contact__line--web">www.solennespa.com
      <svg viewBox="0 0 16 16" aria-hidden="true"><circle cx="8" cy="8" r="6.5" fill="var(--frame)"/><path d="M1.5 8h13M8 1.5c-3 3-3 10 0 13M8 1.5c3 3 3 10 0 13" stroke="var(--panel)" stroke-width="1" fill="none"/></svg></p>
    <p class="contact__line contact__line--address">Lindenweg 42, 91180 Heideck
      <svg viewBox="0 0 16 16" aria-hidden="true"><path fill="var(--frame)" d="M8 1a4.5 4.5 0 0 0-4.5 4.5C3.5 9 8 13 8 13s4.5-4 4.5-7.5A4.5 4.5 0 0 0 8 1z"/><circle cx="8" cy="5.5" r="1.6" fill="var(--panel)"/><rect x="3" y="13.5" width="10" height="1.5" fill="var(--frame)"/></svg></p>
  </div>
</section>

<section class="card card--back" aria-label="Rückseite">
  <svg class="back-lines" viewBox="115 497 730 425" preserveAspectRatio="none" aria-hidden="true">
    <g fill="none" stroke="var(--line)" stroke-width="3">
      <polyline points="378,497 180,690 555,922" vector-effect="non-scaling-stroke"/>
      <polyline points="610,497 793,685 555,922" vector-effect="non-scaling-stroke"/>
      <polygon points="778,528 668,637 770,745 880,636" vector-effect="non-scaling-stroke"/>
    </g>
  </svg>
  <div class="brand">
    <div class="brand__name">SOLENNE</div>
    <div class="brand__tagline">SPA &amp; AESTHETICS</div>
  </div>
</section>

</body>
</html>
```